Letterhead for Conveyancing Company

Use existing logo to create a letterhead for a conveyancing company. Must be able to be used in Microsoft Word. Easy to read and professional.
Contact information to be at the bottom.
Bright Wren Conveyancing Pty Ltd
ACN 621 984 736PO Box 535 Campbelltown SA 5074
Mobile - 0461273985
Web address - www.brightwrenconveyancing.com.au

Requirements
Must have
• Logo and contact details.
• Simple and professional.

```html
<!DOCTYPE html>
<html lang="en">
<head>
<meta charset="utf-8">
<title>Bright Wren Conveyancing – Letterhead</title>
<link rel="stylesheet" href="https://fonts.googleapis.com/css2?family=Roboto:wght@400;500;700&family=Mulish:wght@700&display=swap">
<style>
  :root {
    --backdrop: #4e4b4a;
    --paper: #fafafa;
    --ink: #6b6b6b;
    --ink-strong: #555555;
    --brand-grey: #7f8285;
    --brand-pink: #d84f8c;
    --footer-text: #ffffff;
    --signature: #4a6a9a;
  }
  * { margin: 0; padding: 0; box-sizing: border-box; }
  html, body { width: 1062px; height: 1200px; overflow: hidden; background: var(--backdrop); }
  body { position: relative; font-family: "Roboto", Arial, sans-serif; color: var(--ink); }

  .letterhead {
    position: absolute; left: 200px; top: 132px; width: 662px; height: 936px;
    background: var(--paper);
  }
  .brand {
    position: absolute; right: 52px; top: 206px; text-align: right;
    font-family: "Roboto", Arial, sans-serif; font-weight: 700;
    color: var(--brand-pink); line-height: 1.05;
  }
  .brand-name { display: block; font-size: 30px; letter-spacing: -0.5px; }
  .brand-sub { display: block; font-size: 11px; letter-spacing: 2.6px; margin-top: 6px; }

  .letter { position: absolute; left: 41px; width: 579px; font-size: 10.6px; line-height: 15px; }
  .date { top: 228px; }
  .recipient { top: 274px; }
  .recipient strong { font-weight: 500; color: var(--ink-strong); }
  .salutation { top: 364px; }
  .body { top: 394px; }
  .body p { text-align: justify; margin-bottom: 15px; }

  .sign-off { position: absolute; left: 41px; top: 740px; font-size: 10.6px; line-height: 15px; }
  .sign-name { font-weight: 500; color: var(--ink-strong); }
  .signature {
    position: absolute; left: 27px; top: 758px; width: 151px; height: 32px;
    background: linear-gradient(90deg, rgba(74,106,154,0.18), rgba(74,106,154,0.05));
    border-radius: 4px;
  }
  .sign-role { position: absolute; left: 41px; top: 801px; font-size: 10.6px; }

  .footer {
    position: absolute; left: 0; bottom: 0; width: 100%; height: 52px;
    background: var(--brand-pink); color: var(--footer-text); text-align: center;
  }
  .footer-company { font-family: "Mulish", Arial, sans-serif; font-weight: 700; font-size: 13px; padding-top: 9px; }
  .footer-contact {
    display: flex; justify-content: center; align-items: center; gap: 5px;
    font-size: 10.5px; margin-top: 4px;
  }
  .footer-contact svg { width: 9px; height: 9px; fill: none; stroke: var(--footer-text); stroke-width: 1.4; }
  .footer-contact .item { display: inline-flex; align-items: center; gap: 5px; margin-right: 3px; }
</style>
</head>
<body>
  <main class="letterhead">
    <div class="brand">
      <span class="brand-name">Bright Wren</span>
      <span class="brand-sub">CONVEYANCING</span>
    </div>

    <div class="letter date">30/20/2016</div>

    <div class="letter recipient">
      <strong>Mr. XYZ Smith</strong><br>
      123, Street No. 123,<br>
      City Name<br>
      Pincode-123456
    </div>

    <div class="letter salutation">Dear Sir,</div>

    <div class="letter body">
      <p>Lorem Ipsum is simply dummy text of the printing and typesetting industry. Lorem Ipsum has been the industry's standard dummy text ever since the 1500s, when an unknown printer took a galley of type and scrambled it to make a type specimen book. It has survived not only five centuries, but also the leap into electronic typesetting, remaining essentially unchanged. It was popularised in the 1960s with the release of Lettrex sheets containing Lorem Ipsum passages, and more recently with desktop publishing software like Alder PageCraft including versions of Lorem Ipsum.</p>
      <p>Lorem Ipsum is simply dummy text of the printing and typesetting industry. Lorem Ipsum has been the industry's standard dummy text ever since the 1500s, when an unknown printer took a galley of type and scrambled it to make a type specimen book. It has survived not only five centuries, but also the leap into electronic typesetting, remaining essentially unchanged. It was popularised in the 1960s with the release of Lettrex sheets containing Lorem Ipsum passages, and more recently with desktop publishing software like Alder PageCraft including versions of Lorem Ipsum.</p>
      <p>Lorem Ipsum is simply dummy text of the printing and typesetting industry. Lorem Ipsum has been the industry's standard dummy text ever since the 1500s, when an unknown printer took a galley of type and scrambled it to make a type specimen book.</p>
      <p>Lorem Ipsum is simply dummy text of the printing and typesetting industry. Lorem Ipsum has been the industry's standard dummy text ever since the 1500s, when an unknown printer took a galley of type and scrambled it to make a type specimen book.</p>
    </div>

    <div class="sign-off sign-name">Your Name</div>
    <div class="signature" role="img" aria-label="Handwritten signature"></div>
    <div class="sign-role">CEO &nbsp;|&nbsp; Owner</div>

    <footer class="footer">
      <div class="footer-company">Bright Wren Conveyancing Pty Ltd</div>
      <div class="footer-contact">
        <span class="item">
          <svg viewBox="0 0 10 10" aria-hidden="true"><circle cx="5" cy="5" r="4"/><path d="M1 5h8M5 1c-2 2.5-2 5.5 0 8M5 1c2 2.5 2 5.5 0 8"/></svg>
          www.brightwrenconveyancing.com.au
        </span>
        <span class="item">
          <svg viewBox="0 0 10 10" aria-hidden="true"><path d="M5 9.5C2.5 6.5 2 5.2 2 4a3 3 0 0 1 6 0c0 1.2-.5 2.5-3 5.5z"/><circle cx="5" cy="4" r="1"/></svg>
          PO Box 862 Marlow Heights SA 5093
        </span>
        <span class="item">
          <svg viewBox="0 0 10 10" aria-hidden="true"><path d="M5 1v8M1 5h8M2.2 2.2l5.6 5.6M7.8 2.2L2.2 7.8"/></svg>
          ACN 738 215 490
        </span>
      </div>
    </footer>
  </main>
</body>
</html>
```